Anzeigengestaltung für Sanitätshaus mit orthopädischer Werkstatt
Zielgruppe
Wir sind ein Sanitätshaus mit orthopädischer Werkstatt. Unsere Firma versorgt Patienten von 2-100 Jahren mit Medizinprodukten. Diese sind z.B. Bandagen, Orthesen, Prothesen, Kompressionsstrümpfe...aber auch Pflegebetten, Rollstühle, Toilettenstühle für ältere pflegebedürftige Patienten. Für die letzteren Hilfsmittel suchen wir einen möglichst jungen (20-40 Jahre) Außendienst. Dieser sollte vielleicht einen medizinischen Beruf gelernt haben. Ist aber kein Zwang. Auf jeden Fall sollte er handwerklich begabt sein. Es muß ein offener, freundicher Mensch mit positiver Ausstrahlung sein der offen ist für neue Aufgaben! Die Arbeit ist sehr abwechslungsreich. Eine Weiterbildung (Dauer 2 Tage im Schulungszentrum) zum Mediziprodukteberater und zahlreiche weitere Schulungen über Hilfsmittel, werden dem neuen Mitarbeiter als Grundlage zur Ausübung des Berufes zur Verfügung gestellt. Der Mitarbeiter fährt nach der ausgiebigen Einarbeitungszeit selbstständig mit unserem Lieferwagen zu Partienten, Pflegediensten, Krankenhäuser und liefert dort Reha-Hilfsmittel aus oder past Medizinprodukte an.
Aufgabenstellung
Im Anhang lade ich unsere jetzige, selbst verfasste Anzeige mit dem Logo von unserer Firma. Wir möchten unsere 'Stellenanzeige' bei Quasselhof, Blinkpost und Lumatok laden. Um diese Anzeige auf diesen Kanälen schalten zu können, müssen diese quadratisch sein.
Wichtig ist! Der Text zur Anzeige soll nicht verändert werden.
Ich habe noch ein tolles Bild was bei Pixavera gelistet ist für diese Anzeige:
https://bilder.pixavera-beispiel.de/de/search?serie_id=918346071&asset_id=918346071

```html
<!DOCTYPE html>
<html lang="de">
<head>
<meta charset="utf-8">
<title>Stellenanzeige Reha-Außendienst</title>
<link href="https://fonts.googleapis.com/css2?family=Fira+Sans+Extra+Condensed:wght@400;500;600&family=Open+Sans:wght@400;700&display=swap" rel="stylesheet">
<style>
  :root {
    --brand-red: #e30045;
    --band-grey: #a3a3a3;
    --text-grey: #8a8a8a;
    --dark-grey: #6e6e6e;
    --white: #ffffff;
  }
  * { margin: 0; padding: 0; box-sizing: border-box; }
  html, body { width: 1200px; height: 1153px; overflow: hidden; background: var(--white); }
  .ad { position: relative; width: 1200px; height: 1153px; background: var(--white); font-family: "Fira Sans Extra Condensed", sans-serif; }

  .brand { position: absolute; left: 0; top: 88px; width: 617px; text-align: center; }
  .brand-name { font-family: "Fira Sans Extra Condensed", sans-serif; font-weight: 600; color: var(--brand-red); font-size: 42px; line-height: 1.1; white-space: nowrap; }
  .brand-tagline { font-family: "Fira Sans Extra Condensed", sans-serif; font-weight: 400; color: var(--text-grey); font-size: 23px; margin-top: 12px; }

  .headline-band { position: absolute; left: 0; top: 239px; width: 617px; height: 126px; background: var(--band-grey); padding: 26px 0 0 35px; }
  .headline-band h1 { font-family: "Open Sans", sans-serif; font-weight: 700; color: var(--white); font-size: 25px; line-height: 35px; white-space: nowrap; }

  .photo { position: absolute; left: 0; top: 497px; width: 617px; height: 656px;
    background: linear-gradient(180deg, #fbf4ee 0%, #f3e3d6 30%, #c9c2b4 55%, #7f8a6a 78%, #b98a78 100%); }

  .intro { position: absolute; left: 28px; width: 585px; color: var(--text-grey); font-weight: 600; font-size: 17.5px; line-height: 25px; white-space: nowrap; }
  .intro-company { top: 402px; }
  .intro-offer { top: 500px; }

  .info-panel { position: absolute; left: 617px; top: 0; width: 583px; height: 1014px; background: var(--brand-red); color: var(--white); }
  .info-panel h2 { position: absolute; left: 84px; font-family: "Open Sans", sans-serif; font-weight: 700; font-size: 29px; letter-spacing: 0.3px; }
  .info-panel ul { position: absolute; left: 67px; list-style: none; width: 505px; }
  .info-panel li { position: relative; padding-left: 17px; font-weight: 500; font-size: 20px; line-height: 26px; white-space: nowrap; }
  .info-panel li::before { content: ""; position: absolute; left: 0; top: 11px; width: 7px; height: 7px; background: var(--white); }
  .divider { position: absolute; left: 51px; width: 482px; height: 2px; background: var(--white); }

  .profile-title { top: 72px; }
  .profile-list { top: 127px; }
  .profile-list li + li { margin-top: 27px; }
  .divider-1 { top: 367px; }
  .tasks-title { top: 426px; }
  .tasks-list { top: 482px; }
  .tasks-list li + li { margin-top: 27px; }
  .divider-2 { top: 684px; }
  .offer-title { top: 736px; }
  .offer-list { top: 790px; }
  .offer-list li + li { margin-top: 26px; }

  .apply { position: absolute; left: 617px; top: 1014px; width: 583px; text-align: center; }
  .apply-call { color: var(--brand-red); font-weight: 600; font-size: 23.5px; margin-top: 22px; }
  .apply-contact { color: var(--dark-grey); font-weight: 600; font-size: 18.5px; line-height: 26px; margin-top: 17px; }
</style>
</head>
<body>
<main class="ad">
  <div class="brand">
    <div class="brand-name">Sanitätshaus Albrecht</div>
    <div class="brand-tagline">Ihre Fachberatung für Reha und Pflege.</div>
  </div>

  <div class="headline-band">
    <h1>Junger, dynamischer Reha-Außendienstler/<br>Medizinprodukteberater gesucht!</h1>
  </div>

  <div class="photo" role="img" aria-label="Foto: junger Mann schiebt einen älteren Herrn im Rollstuhl auf einem Gehweg in warmem Abendlicht"></div>

  <p class="intro intro-company">Unser Familienunternehmen „Sanitätshaus &amp; orthopädische Werkstatt Albrecht“<br>versorgt Menschen mit medizinischen Hilfsmitteln und Produkten für Gesundheit<br>und Wohlbefinden.</p>
  <p class="intro intro-offer">Wir bieten zukunftssichere und abwechslungsreiche Tätigkeiten mit hervorragenden<br>Perspektiven im Gesundheitswesen.</p>

  <section class="info-panel">
    <h2 class="profile-title">IHR PROFIL</h2>
    <ul class="profile-list">
      <li>erfolgreich abgeschlossene Berufsausbildung<br>in einem (möglichst) medizinischen Beruf</li>
      <li>gute handwerkliche Fähigkeiten</li>
      <li>zuverlässig, zielstrebig, verantwortungsbewusst,<br>teamfähig, selbstständiges Arbeiten, soziale Kompetenz</li>
    </ul>
    <div class="divider divider-1"></div>

    <h2 class="tasks-title">IHRE AUFGABEN</h2>
    <ul class="tasks-list">
      <li>Auslieferung/Reparatur und Beratung von Rollstühlen,<br>Krankenbetten, und weiteren Reha- und Medizinprodukten</li>
      <li>Beratung und Verkauf von Medizinprodukten</li>
      <li>organisatorische Aufgaben und Planungen am PC</li>
    </ul>
    <div class="divider divider-2"></div>

    <h2 class="offer-title">UNSER ANGEBOT</h2>
    <ul class="offer-list">
      <li>zukunftssicherer Arbeitsplatz 40 Stunden/Woche</li>
      <li>individuelle Einarbeitung mit fortlaufenden Qualifikationen</li>
      <li>Ausbildung zu Medizinprodukteberater</li>
      <li>gutes Arbeitsklima im Familienunternehmen</li>
    </ul>
  </section>

  <section class="apply">
    <p class="apply-call">Überzeugen Sie uns durch Ihre aussagekräftige Bewerbung!</p>
    <p class="apply-contact">Bewerbungen an: info@albrecht-reha-beispiel.de (nur als PDF) oder<br>Sanitätshaus Albrecht GmbH, Lindenweg 7, 09999 Musterbach</p>
  </section>
</main>
</body>
</html>
```